i need a business card for a plumbing company in california

we are a drain cleaning , maintenance plumbing company who is starting new marketing campaign for a tatrench-less pipe installation department .

Target Market(s)

the professional who appreciates time and quality workmanship.

Industry/Entity Type

Plumbing

Colors
0655a3
ec1f27

Requirements
Must have
• the second logo needs to be included
Nice to have
• a focus on the services offered
Should not have
• any underlined words on the brief

```html
<!DOCTYPE html>
<html lang="en">
<head>
<meta charset="UTF-8">
<title>Crestline Plumbing – Business Card</title>
<link href="https://fonts.googleapis.com/css2?family=Arimo:wght@400;700&family=Lato:wght@400&display=swap" rel="stylesheet">
<style>
  :root {
    --page-bg: #ece9e4;
    --card-bg: #070707;
    --brand-red: #ec1f27;
    --brand-grey: #a3a3a3;
    --text-light: #c9c9c9;
    --text-muted: #9c9c9c;
  }
  * { margin: 0; padding: 0; box-sizing: border-box; }
  html, body {
    width: 1200px;
    height: 675px;
    overflow: hidden;
    background: var(--page-bg);
  }
  .stage {
    position: relative;
    width: 1200px;
    height: 675px;
  }
  .card {
    position: absolute;
    left: 340px;
    width: 520px;
    height: 294px;
    background: var(--card-bg);
    box-shadow: 0 4px 14px rgba(0,0,0,0.25);
    color: var(--text-light);
  }
  .card--front { top: 25px; }
  .card--back { top: 356px; }

  /* brand name lockup */
  .brand {
    display: flex;
    align-items: center;
    gap: 7px;
    font-family: "Arimo", Arial, sans-serif;
    font-weight: 700;
    color: var(--brand-grey);
    white-space: nowrap;
  }
  .brand__dot {
    border-radius: 50%;
    background: var(--brand-red);
    flex: none;
  }

  /* front */
  .front__brand {
    position: absolute;
    top: 98px;
    left: 0;
    right: 0;
    justify-content: center;
    font-size: 22px;
  }
  .front__brand .brand__dot { width: 14px; height: 14px; }
  .front__rule {
    position: absolute;
    top: 146px;
    left: 95px;
    width: 337px;
    height: 3px;
    background: var(--brand-red);
  }
  .front__services {
    position: absolute;
    top: 154px;
    left: 60px;
    right: 60px;
    text-align: center;
    font-family: "Lato", Arial, sans-serif;
    font-size: 11px;
    line-height: 15px;
    color: var(--text-muted);
  }

  /* back */
  .back__brand {
    position: absolute;
    top: 34px;
    left: 29px;
    font-size: 17px;
  }
  .back__brand .brand__dot { width: 11px; height: 11px; }
  .back__web {
    position: absolute;
    top: 22px;
    right: 20px;
    text-align: left;
    font-family: "Arimo", Arial, sans-serif;
    font-size: 8.5px;
    line-height: 12px;
    color: var(--text-muted);
  }
  .owner {
    position: absolute;
    top: 122px;
    left: 210px;
    font-family: "Arimo", Arial, sans-serif;
  }
  .owner__name {
    font-size: 16px;
    color: var(--text-light);
    letter-spacing: 0.2px;
  }
  .owner__rule {
    position: absolute;
    top: 28px;
    left: 0;
    width: 97px;
    height: 3px;
    background: var(--brand-red);
  }
  .owner__title {
    position: absolute;
    top: 20px;
    left: 99px;
    font-size: 11px;
    color: var(--text-muted);
  }
  .contacts {
    position: absolute;
    bottom: 24px;
    left: 54px;
    right: 54px;
    display: flex;
    justify-content: space-between;
    font-family: "Arimo", Arial, sans-serif;
    font-size: 8.5px;
    color: var(--text-muted);
  }
  .contacts__item {
    display: flex;
    align-items: center;
    gap: 5px;
  }
  .contacts__dot {
    width: 10px;
    height: 10px;
    border-radius: 50%;
    flex: none;
  }
  .contacts__dot--blue { background: #0655a3; }
  .contacts__dot--red { background: var(--brand-red); }
  .contacts__dot--phone { background: transparent; }
</style>
</head>
<body>
<main class="stage">

  <section class="card card--front" aria-label="Card front">
    <div class="brand front__brand">
      <span>Crestline Plumbing</span>
      <span class="brand__dot"></span>
    </div>
    <div class="front__rule"></div>
    <p class="front__services">Virgin Trench-Less Sewer Installs &amp; Replacements – Pipe Bursting &amp;<br>Pipe Piercing Install, Replacem Pipe Enlargement Pull &amp; GO</p>
  </section>

  <section class="card card--back" aria-label="Card back">
    <div class="brand back__brand">
      <span>Crestline Plumbing</span>
      <span class="brand__dot"></span>
    </div>
    <div class="back__web">
      www.CrestlinePlumbing.com<br>
      info@CrestlinePlumbing.com
    </div>
    <div class="owner">
      <div class="owner__name">Marco Delgado Jr</div>
      <div class="owner__rule"></div>
      <div class="owner__title">Owner</div>
    </div>
    <div class="contacts">
      <div class="contacts__item">
        <span class="contacts__dot contacts__dot--blue"></span>
        <span>Facebook@CrestlinePlumb</span>
      </div>
      <div class="contacts__item">
        <span class="contacts__dot contacts__dot--red"></span>
        <span>CrestlinePlumbing</span>
      </div>
      <div class="contacts__item">
        <svg class="contacts__dot contacts__dot--phone" viewBox="0 0 10 10" aria-hidden="true">
          <path d="M2.2 1h1.6l.8 2-1 .7a5.5 5.5 0 0 0 2.7 2.7l.7-1 2 .8v1.6c0 .6-.5 1.2-1.2 1.2A7.6 7.6 0 0 1 1 2.2C1 1.5 1.6 1 2.2 1z" fill="#ec1f27"/>
        </svg>
        <span>Phone: 2095550187</span>
      </div>
    </div>
  </section>

</main>
</body>
</html>
```